Business Card Design

Electronic Security
Alarm Systems
CCTV
Electronic Access Control
Security System Integration

Industry/Entity Type

Business

Contact Information for Business Card

Gareth Linwood
PO Box 862
Yarrowdale Qld 4173
Phone 07 38265140
Mob 0428637291

```html
<!DOCTYPE html>
<html lang="en">
<head>
<meta charset="utf-8">
<title>Valtro Protective Systems – Business Cards</title>
<link rel="stylesheet" href="https://fonts.googleapis.com/css2?family=Open+Sans:wght@400;600;700&display=swap">
<style>
  :root {
    --canvas: #ececec;
    --card: #ffffff;
    --blue: #1e8fc4;
    --orange: #f4a12b;
    --ink: #2e2e2e;
    --muted: #8a8a8a;
    --faint: #dbe9f3;
  }
  * { margin: 0; padding: 0; box-sizing: border-box; }
  html, body { width: 1200px; height: 1200px; overflow: hidden; }
  body {
    background: var(--canvas);
    font-family: "Open Sans", Arial, sans-serif;
    color: var(--ink);
    position: relative;
  }
  .card {
    position: absolute;
    left: 190px;
    width: 820px;
    height: 500px;
    background: var(--card);
    box-shadow: 0 8px 24px rgba(0,0,0,0.10);
    overflow: hidden;
  }
  .card--back { top: 70px; }
  .card--front { top: 630px; }

  .brand { position: absolute; display: flex; align-items: center; gap: 14px; }
  .brand__dot { background: var(--blue); border-radius: 50%; }
  .brand__name { font-weight: 700; color: var(--ink); letter-spacing: 1px; }
  .brand__rule { width: 2px; background: var(--ink); align-self: stretch; }
  .brand__tagline { font-weight: 600; color: var(--ink); line-height: 1.05; }

  .card--back .brand { left: 60px; top: 70px; }
  .card--back .brand__dot { width: 22px; height: 22px; }
  .card--back .brand__name { font-size: 40px; }
  .card--back .brand__tagline { font-size: 13px; }

  .card--front .brand { left: 120px; top: 190px; }
  .card--front .brand__dot { width: 34px; height: 34px; }
  .card--front .brand__name { font-size: 66px; }
  .card--front .brand__tagline { font-size: 19px; }

  .person { position: absolute; left: 60px; top: 205px; }
  .person__name { font-size: 26px; font-weight: 700; color: var(--blue); }
  .person__title { font-size: 14px; color: var(--muted); margin-top: 2px; }

  .band { position: absolute; left: 0; right: 0; top: 290px; }
  .band__blue { height: 7px; background: var(--blue); }
  .band__orange { height: 2px; background: var(--orange); }

  .divider { position: absolute; left: 420px; top: 60px; width: 2px; height: 200px; background: var(--ink); }

  .services { position: absolute; left: 450px; top: 66px; list-style: none; }
  .services li { display: flex; align-items: center; gap: 10px; font-size: 17px; line-height: 38px; }
  .services li::before {
    content: ""; width: 9px; height: 9px; background: var(--blue);
  }

  .contact { position: absolute; left: 260px; top: 330px; font-size: 16px; line-height: 28px; }
  .contact strong { font-weight: 700; }
  .contact .sep { color: var(--muted); margin: 0 12px; }

  .decor { position: absolute; border-radius: 50%; background: var(--faint); opacity: 0.75; }
  .card--back .decor { width: 220px; height: 220px; right: -40px; bottom: -20px; }
  .card--front .decor { width: 300px; height: 300px; right: -60px; bottom: -40px; }
</style>
</head>
<body>
  <section class="card card--back">
    <div class="brand">
      <span class="brand__dot"></span>
      <span class="brand__name">VALTRO</span>
      <span class="brand__rule"></span>
      <span class="brand__tagline">Valtro<br>Protective<br>Systems</span>
    </div>
    <div class="person">
      <p class="person__name">Gareth Linwood</p>
      <p class="person__title">Title Goes Here</p>
    </div>
    <div class="divider"></div>
    <ul class="services">
      <li>Electronic Security</li>
      <li>Alarm Systems</li>
      <li>CCTV</li>
      <li>Electronic Access Control</li>
      <li>Security System Integration</li>
    </ul>
    <div class="band"><div class="band__blue"></div><div class="band__orange"></div></div>
    <div class="contact">
      <p>PO Box 862 Yarrowdale Qld 4173</p>
      <p><strong>Ph:</strong> 07 38265140<span class="sep">|</span><strong>Mob:</strong> 0428637291</p>
    </div>
    <div class="decor" role="img" aria-label="Faint brand emblem decoration"></div>
  </section>

  <section class="card card--front">
    <div class="brand">
      <span class="brand__dot"></span>
      <span class="brand__name">VALTRO</span>
      <span class="brand__rule"></span>
      <span class="brand__tagline">Valtro<br>Protective<br>Systems</span>
    </div>
    <div class="decor" role="img" aria-label="Faint brand emblem decoration"></div>
  </section>
</body>
</html>
```